We need a design for a clothing tag for our summer hats & sandals line. Tag should be 2.25" high by 2" wide with a little hole punch circle in the top center. The brand is "Coral Drift" so it should have that name on the tag & then I would also like "Summer Apparel" on the tag somewhere lower on the tag perhaps in a bit smaller font. It should obviously be summer themed- with a picture of a beach or sand- something to that effect. Our previous brand was "Lumen Days"- I have attached that artwork so you can get an idea of what we are looking for.

Logo Text

Coral Drift

```html
<!DOCTYPE html>
<html lang="en">
<head>
<meta charset="utf-8">
<title>Coral Drift – Summer Apparel Tag</title>
<link rel="stylesheet" href="https://fonts.googleapis.com/css2?family=Archivo+Black&family=Lobster&display=swap">
<style>
  :root {
    --sky-top: #3f5f94;
    --sky-low: #7b93b8;
    --sea: #5fa9ad;
    --sea-shallow: #93b9b3;
    --sand: #b3ab9c;
    --sand-deep: #a59c8c;
    --shade: rgba(20, 30, 60, 0.22);
    --white: #ffffff;
    --price-green: #1b5a4a;
    --brand-yellow: #e3ef7e;
    --tagline-aqua: #7fd2d6;
  }
  * { margin: 0; padding: 0; box-sizing: border-box; }
  html, body {
    width: 1067px;
    height: 1200px;
    overflow: hidden;
    background: var(--white);
  }
  .tag {
    position: relative;
    width: 1067px;
    height: 1200px;
    overflow: hidden;
  }
  .beach-scene {
    position: absolute;
    inset: 0;
    background:
      linear-gradient(180deg, var(--shade), var(--shade)),
      linear-gradient(180deg,
        var(--sky-top) 0%,
        var(--sky-low) 48%,
        var(--sea) 53%,
        var(--sea-shallow) 62%,
        var(--sand) 72%,
        var(--sand-deep) 100%);
  }
  .hole-punch {
    position: absolute;
    left: 480px;
    top: 63px;
    width: 106px;
    height: 106px;
    border-radius: 50%;
    background: var(--white);
  }
  .price-badge {
    position: absolute;
    left: 707px;
    top: 41px;
    width: 292px;
    height: 292px;
    border-radius: 50%;
    background: var(--white);
    display: flex;
    align-items: center;
    justify-content: center;
    font-family: "Archivo Black", "Arial Black", sans-serif;
    color: var(--price-green);
    line-height: 1;
  }
  .price-badge .currency { font-size: 58px; align-self: flex-start; margin-top: 102px; }
  .price-badge .dollars { font-size: 130px; }
  .price-badge .cents { font-size: 58px; align-self: flex-start; margin-top: 102px; }
  .brand-name {
    position: absolute;
    left: 230px;
    top: 420px;
    font-family: "Lobster", cursive;
    font-size: 200px;
    line-height: 0.95;
    color: var(--brand-yellow);
  }
  .brand-name .line { display: block; }
  .brand-name .line-two { padding-left: 40px; }
  .tagline {
    position: absolute;
    left: 0;
    right: 0;
    top: 990px;
    text-align: center;
    font-family: "Lobster", cursive;
    font-size: 74px;
    color: var(--tagline-aqua);
  }
</style>
</head>
<body>
  <main class="tag">
    <div class="beach-scene" role="img" aria-label="Photo of a tropical beach with palm trees, blue sky, turquoise sea and white sand"></div>
    <div class="hole-punch" aria-hidden="true"></div>
    <div class="price-badge" aria-label="Price $3.99">
      <span class="currency">$</span><span class="dollars">3</span><span class="cents">99</span>
    </div>
    <h1 class="brand-name">
      <span class="line line-one">Coral</span>
      <span class="line line-two">Drift</span>
    </h1>
    <p class="tagline">Summer Apparel</p>
  </main>
</body>
</html>
```